Flyer-Design für Kurierdienst
Der gedruckte Flyer ist heute bei uns angekommen. Wir sind mit der Arbeit sehr zufrieden.
Zielgruppe
Wir sind ein Kurierdienst in Frankfurt am Main. Der Flyer soll auf unsere drei Kerndienstleistungen aufmerksam machen. Diese sind Direktfahrten innerhalb von Frankfurt, Deutschland und Europa, der nationale Versand über Nacht sowie der internationale Expressversand.
Unsere Zielgruppe sind ausschließlich Firmenkunden in Frankfurt. Vor allem möchten wir mit dem Flyer anspruchsvolle Kunden wie z.B. Anwaltskanzleien und Finanzdienstleister erreichen. Wir bieten einen Rundum-Service, geschulte Fahrer und feste Ansprechpartner (kein Callcenter).
Eine genauere Beschreibung unserer Dienstleistungen hängt an bzw. sind auf unserer Internetseite unter www.lindenhofmobil.com zu finden.
Aufgabenstellung
Wir haben uns einen zwei- oder vierseitigen DIN-Lang Flyer vorgestellt. Farblich sollte sich der Flyer am blau aus unserem Logo orientieren. Das angehangene "Die Lerche" Logo darf nur in Verbindung mit dem nationalen Versand über Nacht aufgeführt werden. Unsere Telefonnummer solle auf der Frontseite deutlich hervorgehoben sein.

```html
<!DOCTYPE html>
<html lang="de">
<head>
<meta charset="utf-8">
<title>Lindenhof Mobil – Leistungen</title>
<link rel="stylesheet" href="https://fonts.googleapis.com/css2?family=Arimo:ital,wght@0,400;0,700;1,700&display=swap">
<style>
  :root {
    --text: #555759;
    --heading-blue: #2b5f9e;
    --icon-tone: #dbe7f3;
    --sky-light: #dfe8f1;
    --sky-mid: #a9bfd6;
    --sky-dark: #5f7f9f;
    --info-grey: #b3b4b6;
    --wedge-blue: #5ab8f5;
    --white: #ffffff;
  }
  * { margin: 0; padding: 0; box-sizing: border-box; }
  html, body { width: 1143px; height: 1200px; overflow: hidden; background: var(--white); }
  body { position: relative; font-family: "Arimo", Arial, sans-serif; color: var(--text); font-size: 18px; line-height: 24.4px; }

  .hero-photo {
    position: absolute; left: 0; top: 0; width: 1143px; height: 185px;
    background: linear-gradient(100deg, var(--sky-mid) 0%, var(--sky-light) 38%, #f2f5f8 55%, var(--sky-mid) 72%, var(--sky-dark) 100%);
  }

  .intro { position: absolute; left: 49px; top: 224px; white-space: nowrap; }

  .section-title {
    position: absolute; left: 49px; top: 372px;
    font-size: 26px; font-weight: 700; color: var(--heading-blue); line-height: 30px;
  }

  .service { position: absolute; white-space: nowrap; }
  .service-title { font-weight: 700; }
  .service p + p { margin-top: 12px; }
  .service .brand { font-weight: 700; font-style: italic; }

  .service--direct { left: 223px; top: 430px; }
  .service--overnight { left: 223px; top: 677px; }
  .service--international { left: 780px; top: 224px; }
  .service--partner { left: 779px; top: 424px; }

  .service-icon { position: absolute; border-radius: 50%; background: var(--icon-tone); }
  .service-icon--direct { left: 84px; top: 436px; width: 84px; height: 84px; }
  .service-icon--overnight { left: 82px; top: 682px; width: 90px; height: 90px; }
  .service-icon--international { left: 637px; top: 229px; width: 100px; height: 100px; }

  .partner-mark {
    position: absolute; left: 640px; top: 437px;
    display: flex; align-items: center; gap: 8px;
    font-weight: 700; font-size: 18px; color: var(--heading-blue);
  }
  .partner-mark .square { width: 16px; height: 16px; background: var(--heading-blue); }

  .contact-box {
    position: absolute; left: 628px; top: 864px; width: 457px; height: 175px;
    background: var(--info-grey); color: var(--white); padding: 23px 29px;
    white-space: nowrap;
  }
  .contact-box .contact-title { font-weight: 700; }
  .contact-box .phone { margin-top: 14px; font-size: 20px; }

  .footer-wedge { position: absolute; left: 0; top: 1080px; }
</style>
</head>
<body>
  <div class="hero-photo" role="img" aria-label="Fotografie: Blick nach oben auf moderne Bürohochhäuser mit Glasfassaden"></div>

  <p class="intro">Kurierversand ist Vertrauenssache und bei uns erhalten<br>Sie mehr als nur den Versand von A nach B. Getreu dem<br>Motto: Feste Anprechpartner statt Callcenter und fester<br>Fahrerstamm statt ständig neuer Kurierfahrer.</p>

  <h2 class="section-title">Wir bieten an</h2>

  <div class="service-icon service-icon--direct" role="img" aria-label="Illustration: Lieferwagen für Direktfahrten"></div>
  <div class="service service--direct">
    <p><span class="service-title">Direktfahrten</span><br>Wir fahren jeden Tag für Sie, auch<br>nachts und an Feiertagen.<br>Deutschland- und Europaweit – vom<br>Briefumschlag bis zur Europalette.</p>
    <p>Sie erhalten auf Wunsch eine<br>kostenfreie Empfangsbestätigung<br>per e-Mail oder Fax.</p>
  </div>

  <div class="service-icon service-icon--overnight" role="img" aria-label="Illustration: Hand, die ein Paket übergibt"></div>
  <div class="service service--overnight">
    <p><span class="service-title">Nationaler Overnight-Versand</span><br>Profitieren Sie als Lindenhof Mobil<br>Kunde von unserer Anbindung an<br>das leistungsstarke und PRÜFWERK<br>zertifizierte (ISO 9001:2008)<br>Netzwerk von <span class="brand">Die Lerche</span>.</p>
    <p>Die Zustellung Ihrer Sendungen<br>erfolgt am nächsten Werktag<br>standardmäßig bis 12:00 Uhr<br>(Inselzustellungen ausgenommen)</p>
    <p>Selbstverständlich sind auch<br>Frühtermine bis 10:00 Uhr,<br>09:00 Uhr oder 08:00 Uhr in<br>viele Orte möglich.</p>
  </div>

  <div class="service-icon service-icon--international" role="img" aria-label="Illustration: Zustellung in zwei Tagen"></div>
  <div class="service service--international">
    <p><span class="service-title">Internationaler Versand</span><br>Egal ob Terminzustellung am<br>nächsten Werktag bis 12:00 Uhr in<br>Paris, Madrid oder Los Angeles –<br>wir sind Ihr Spezialist für eilige<br>internationale Kuriersendungen.</p>
  </div>

  <div class="partner-mark"><span class="square"></span><span>Die Lerche</span></div>
  <div class="service service--partner">
    <p><span class="service-title">Unser Partner</span><br>Mit etwa 250 unabhängigen Kurier-<br>stationen und jahrzehntelanger<br>Erfahrung hat sich <span class="brand">Die Lerche</span><br>zu einem der führenden Kurier-<br>netzbetreibern entwickelt. Dies<br>ermöglicht uns einen zuverlässigen<br>und schnellen Versand für unsere<br>Kunden.</p>
  </div>

  <div class="contact-box">
    <p><span class="contact-title">Wir sind für Sie da</span><br>Gerne können Sie uns von Montag bis Sonntag<br>von 0.00 Uhr bis 24.00 Uhr telefonisch erreichen.</p>
    <p class="phone">Tel.: 069 - 4815260-0</p>
  </div>

  <svg class="footer-wedge" width="1143" height="120" viewBox="0 0 1143 120" aria-hidden="true">
    <polygon points="0,84 1143,6 1143,120 0,120" fill="var(--wedge-blue)"/>
  </svg>
</body>
</html>
```